Outpost Lattice Advisors – Franchise Growth & Development Presentation

Outpost Lattice Advisors is an outsourced franchise sales organization (FSO) that helps franchisors grow their franchise systems without the expense and risk of hiring an internal franchise development team.

We are seeking a professional PowerPoint presentation that will be used to present our services to franchisors, franchise executives, founders, and growth-stage franchise brands.

The presentation should communicate the value of partnering with Outpost Lattice Advisors, including:

• Fractional franchise sales team versus hiring internal staff
• 30+ years of franchise industry experience
• 550+ franchise sales successes
• Immediate access to established franchise broker relationships
• Proven franchise development processes
• Franchise growth strategy and enterprise value creation
• Potential private equity and exit opportunities through franchise expansion

The presentation should feel like a modern consulting, investment, or growth strategy presentation rather than a typical sales brochure. We want strong visual storytelling, custom infographics, professional diagrams, and clean business-oriented design.

The audience includes business owners, franchise founders, franchise executives, and investors who are evaluating growth strategies for their franchise systems.

Target Market(s)

Primary Audience: Emerging franchisors Growth-stage franchise brands Franchise founders Franchise CEOs Franchise presidents Franchise development executives Secondary Audience: Private equity firms Franchise investors Strategic buyers Franchise consultants

Industry/Entity Type

Franchise Development, Private Equity / Business Expansion

Font styles to use
Other font styles liked:
• Use Montserrat for titles and Open Sans for body text.

Requirements
Must have
• Modern professional business design Consistent branding throughout Custom infographics Comparison graphics Broker network ecosystem graphic Enterprise value graphic Easy-to-read charts and visuals Editable PowerPoint format Professional iconography. www.outpostlatticeadvisors.example as reference for colors
Nice to have
• Franchise-related imagery Subtle growth-themed visuals Timeline graphics Data visualization Private equity / valuation style graphics
Should not have
• Cartoon graphics Clip art Overly busy slides Stock-template appearance Bright neon colors Handwritten fonts Excessive text on slides Juvenile or playful design elements

```html
<!DOCTYPE html>
<html lang="en">
<head>
<meta charset="utf-8">
<title>Outpost Lattice Advisors – Franchise Growth Presentation</title>
<link rel="stylesheet" href="https://fonts.googleapis.com/css2?family=Montserrat:wght@400;600;700;800&family=Open+Sans:wght@400;600;700&display=swap">
<style>
:root{
  --navy:#15243d;
  --navy-deep:#101c31;
  --orange:#f5821f;
  --paper:#efedea;
  --white:#ffffff;
  --ink:#1c2536;
  --muted:#6b7280;
  --canvas:#e3e6ea;
}
*{box-sizing:border-box;margin:0;padding:0}
html,body{width:1200px;height:983px;overflow:hidden;background:var(--canvas)}
body{position:relative;font-family:"Open Sans",Arial,sans-serif;color:var(--ink)}
.slide{position:absolute;width:666px;height:375px;transform:scale(0.5661);transform-origin:0 0;overflow:hidden;background:var(--white);box-shadow:0 4px 14px rgba(20,30,50,.18)}
.abs{position:absolute}
.navy{background:var(--navy)}
.paper{background:var(--paper)}
.bar{position:absolute;background:var(--orange)}
.photo{position:absolute}
.brand{position:absolute;font-family:"Montserrat",sans-serif;font-weight:700;font-size:10px;letter-spacing:.4px;line-height:1.15;text-transform:uppercase;color:var(--white)}
.brand--dark{color:var(--navy)}
.title{position:absolute;font-family:"Montserrat",sans-serif;font-weight:400;line-height:1.02;text-transform:uppercase;color:var(--white)}
.title--dark{color:var(--navy)}
.title .hl{color:var(--orange);font-weight:800;display:block}
.title .hl-in{color:var(--orange);font-weight:800}
.lede{position:absolute;font-size:11px;line-height:1.45;color:var(--white)}
.lede b{font-weight:700}
.meta{position:absolute;font-size:11px;line-height:1.3;color:var(--white)}
.meta .hl{color:var(--orange)}
.pageno{position:absolute;font-size:9px;color:var(--navy)}
.issue-list{position:absolute;list-style:none}
.issue-list li{display:flex;align-items:flex-start;gap:10px;font-size:12.5px;line-height:1.5;color:var(--ink);margin-bottom:10px}
.issue-list svg{flex:none;margin-top:3px}
.stat{position:absolute;color:var(--white);font-size:14px;line-height:1.4}
.stat strong{display:block;font-family:"Montserrat",sans-serif;font-weight:700;color:var(--orange);font-size:19px;line-height:1.2}
.compare-box{position:absolute}
.compare-list{position:absolute;list-style:none}
.compare-list li{font-size:15px;line-height:28.5px;display:flex;align-items:center;gap:14px}
.compare-list li::before{content:"";width:5px;height:5px;flex:none}
.compare-list--light li{color:var(--ink)}
.compare-list--light li::before{background:var(--ink)}
.compare-list--dark li{color:var(--white)}
.compare-list--dark li::before{background:var(--orange)}
.side-label{position:absolute;font-family:"Open Sans",sans-serif;font-weight:700;font-size:16px;line-height:1.1;writing-mode:vertical-rl;text-align:center}
.side-label--up{transform:rotate(180deg);color:var(--navy)}
.side-label--down{color:var(--white)}
.wheel-label{position:absolute;font-size:9.5px;font-weight:700;line-height:1.15;color:var(--navy);text-align:center;width:120px}
.node{position:absolute;height:54px;border:1.5px solid var(--navy);border-radius:27px;background:var(--white);display:flex;align-items:center;font-size:9.5px;font-weight:700;line-height:1.2;color:var(--navy)}
.node-icon{position:absolute;width:56px;height:56px;border-radius:50%;background:var(--navy);border:3px solid var(--white);box-shadow:0 0 0 1.5px var(--navy);display:flex;align-items:center;justify-content:center}
.eco-table{position:absolute;border:1px solid #f3c79f;background:var(--white)}
.eco-head{background:var(--navy);color:var(--white);font-size:11px;font-weight:700;text-align:center;line-height:1.2;padding:15px 6px 14px}
.eco-row{height:37.5px;margin:0 12px;border-bottom:1px solid #d7d7d7;display:flex;align-items:center;justify-content:center;font-size:11.5px;color:var(--ink)}
.eco-row:last-child{border-bottom:none}
.card{position:absolute;background:var(--paper);padding:10px 12px}
.card h4{font-family:"Open Sans",sans-serif;font-weight:700;font-size:11.5px;line-height:1.05;color:var(--navy);margin-bottom:8px}
.card p{font-size:7.5px;line-height:1.5;color:#6d6f73;margin-bottom:6px}
.card .ico{display:block;margin-bottom:8px}
.step{position:absolute;background:var(--paper);padding:12px 14px 8px 22px}
.step h4{font-weight:700;font-size:11.5px;color:var(--navy);margin-bottom:6px}
.step p{font-size:7.5px;line-height:1.5;color:#6d6f73}
.dot{position:absolute;width:5px;height:5px;border-radius:50%;background:var(--navy)}
.rule{position:absolute;background:var(--navy)}
.story{position:absolute;color:var(--white)}
.story h3{font-size:11.5px;font-weight:700;line-height:1.15;margin-bottom:12px}
.story p{font-size:7.5px;line-height:1.55;margin-bottom:10px;color:#e6e9ef}
</style>
</head>
<body>

<!-- 01 cover -->
<section class="slide" style="left:21.5px;top:39.6px">
  <div class="photo" role="img" aria-label="Photo of a confident businesswoman holding a notebook in a bright café" style="left:0;top:0;width:666px;height:375px;background:linear-gradient(90deg,#1e2a3f 0%,#2d384c 72%,#8e8a84 84%,#d9d4cc 100%)"></div>
  <div class="abs navy" style="left:0;top:0;width:502px;height:345px"></div>
  <div class="bar" style="left:0;top:0;width:20px;height:185px"></div>
  <div class="bar" style="left:0;top:168px;width:70px;height:17px"></div>
  <div class="bar" style="left:448px;top:0;width:19px;height:185px"></div>
  <div class="bar" style="left:400px;top:168px;width:67px;height:17px"></div>
  <div class="brand" style="left:40px;top:30px">Outpost Lattice Advisors</div>
  <h1 class="title" style="left:86px;top:102px;font-size:28px">Outsourced<span class="hl">Franchise Sales &amp;</span><span class="hl">Growth Experts</span></h1>
  <p class="lede" style="left:87px;top:196px;width:330px">Helping franchisors <b>grow faster without the cost and risk</b> of building an internal franchise development team.</p>
  <p class="meta" style="left:88px;top:275px">Presented by:<br>Dana <span class="hl">MERCER</span></p>
  <p class="meta" style="left:275px;top:275px">Saturday, June 20, 2026</p>
</section>

<!-- 01b cover alt -->
<section class="slide" style="left:411px;top:39.6px">
  <div class="photo" role="img" aria-label="Dimmed photo of a businesswoman in a café behind a navy overlay" style="left:178px;top:0;width:488px;height:375px;background:linear-gradient(90deg,#17243b 0%,#1f2c43 60%,#2a3649 100%)"></div>
  <div class="bar" style="left:0;top:28px;width:30px;height:19px"></div>
  <div class="brand brand--dark" style="left:38px;top:26px;font-size:9px">Outpost Lattice<br>Advisors</div>
  <div class="bar" style="left:152px;top:28px;width:138px;height:19px"></div>
  <div class="bar" style="left:271px;top:28px;width:19px;height:70px"></div>
  <div class="bar" style="left:271px;top:275px;width:19px;height:70px"></div>
  <div class="bar" style="left:0;top:326px;width:290px;height:19px"></div>
  <p class="lede" style="left:28px;top:157px;width:130px;color:var(--ink);font-size:10.5px">Helping franchisors <b>grow faster without the</b> cost and risk of building an internal franchise development team.</p>
  <h1 class="title" style="left:270px;top:146px;font-size:28px">Outsourced<span class="hl">Franchise Sales &amp;</span><span class="hl">Growth Experts</span></h1>
  <p class="meta" style="left:330px;top:275px">Presented by:<br>Dana <span class="hl">MERCER</span></p>
  <p class="meta" style="left:463px;top:275px">Saturday, June 20, 2026</p>
</section>

<!-- 02 challenge -->
<section class="slide" style="left:800.5px;top:39.6px">
  <div class="photo" role="img" aria-label="Dark navy world map with location pins" style="left:0;top:0;width:290px;height:375px;background:radial-gradient(circle at 60% 40%,#24344f 0%,#15243d 70%)"></div>
  <div class="bar" style="left:218px;top:0;width:20px;height:100px"></div>
  <div class="bar" style="left:218px;top:80px;width:102px;height:20px"></div>
  <div class="brand brand--dark" style="left:492px;top:10px;font-size:8.5px">Outpost Lattice Advisors</div>
  <h2 class="title" style="left:12px;top:152px;font-size:23px;line-height:1.18">The challenge<span class="hl">Facing emerging</span><span class="hl">franchisors</span></h2>
  <ul class="issue-list" style="left:357px;top:96px;width:280px">
    <li><svg width="14" height="13" viewBox="0 0 14 13"><path d="M7 0L14 13H0Z" fill="#15243d"/><rect x="6.2" y="4" width="1.6" height="5" fill="#fff"/><rect x="6.2" y="10" width="1.6" height="1.5" fill="#fff"/></svg>Limited franchise sales resources</li>
    <li><svg width="14" height="13" viewBox="0 0 14 13"><ellipse cx="7" cy="10" rx="7" ry="2.5" fill="#15243d"/><rect x="3" y="3" width="8" height="7" rx="2" fill="#15243d"/></svg>Founder wearing too many hats</li>
    <li><svg width="14" height="13" viewBox="0 0 14 13"><circle cx="4" cy="3" r="2.5" fill="#15243d"/><circle cx="10" cy="3" r="2.5" fill="#15243d"/><rect x="1" y="6" width="12" height="3" fill="#15243d"/><rect x="6" y="9" width="2" height="4" fill="#15243d"/></svg>Inconsistent lead follow-up</li>
    <li><svg width="14" height="13" viewBox="0 0 14 13"><circle cx="8.5" cy="5" r="4.2" fill="none" stroke="#15243d" stroke-width="1.8"/><path d="M5.5 8L1 12.5" stroke="#15243d" stroke-width="2.2"/></svg>Difficulty recruiting franchisees</li>
    <li><svg width="14" height="13" viewBox="0 0 14 13"><circle cx="7" cy="3.5" r="3" fill="#15243d"/><path d="M1 13C1 8 13 8 13 13Z" fill="#15243d"/></svg>Lack of broker relationships</li>
    <li><svg width="14" height="14" viewBox="0 0 14 14"><circle cx="7" cy="7" r="7" fill="#15243d"/><text x="7" y="10.5" font-size="9" font-weight="700" text-anchor="middle" fill="#fff" font-family="Open Sans">$</text></svg>High cost of internal franchise<br>development staff</li>
  </ul>
  <div class="bar" style="left:533px;top:282px;width:123px;height:18px"></div>
  <div class="bar" style="left:638px;top:282px;width:18px;height:93px"></div>
  <div class="pageno" style="left:640px;top:361px">02</div>
</section>

<!-- 03 why -->
<section class="slide" style="left:21.5px;top:270px">
  <div class="photo" role="img" aria-label="Navy-tinted photo of business partners shaking hands in an office" style="left:224px;top:0;width:442px;height:355px;background:linear-gradient(120deg,#1a2a44 0%,#15243d 55%,#1d2d47 100%)"></div>
  <div class="bar" style="left:0;top:10px;width:92px;height:20px"></div>
  <div class="bar" style="left:72px;top:10px;width:20px;height:122px"></div>
  <div class="brand" style="left:492px;top:10px;font-size:8.5px">Outpost Lattice Advisors</div>
  <h2 class="title title--dark" style="left:46px;top:150px;font-size:22px;line-height:1.18">Why<span class="hl">Outpost</span><span class="hl">Lattice</span><span class="hl">Advisors</span></h2>
  <div class="stat" style="left:286px;top:46px"><strong>Fractional</strong>franchise sales team</div>
  <div class="stat" style="left:286px;top:112px"><strong>30+ years</strong>franchise industry<br>experience</div>
  <div class="stat" style="left:498px;top:112px"><strong>Deep</strong>broker network<br>relationships</div>
  <div class="stat" style="left:286px;top:202px"><strong>500+</strong>franchise sales successes</div>
  <div class="stat" style="left:498px;top:202px"><strong>Proven</strong>systems and processes</div>
  <div class="stat" style="left:286px;top:264px"><strong>Immediate</strong>execution</div>
  <div class="bar" style="left:522px;top:270px;width:20px;height:105px"></div>
  <div class="bar" style="left:522px;top:355px;width:144px;height:20px"></div>
  <div class="pageno" style="left:640px;top:358px">03</div>
</section>

<!-- 04 cost comparison -->
<section class="slide" style="left:411px;top:270px">
  <h2 class="title title--dark" style="left:12px;top:10px;font-size:23px;line-height:1.17">The cost of hiring<span class="hl">vs. outsourcing</span></h2>
  <div class="bar" style="left:302px;top:28px;width:122px;height:20px"></div>
  <div class="bar" style="left:404px;top:0;width:20px;height:48px"></div>
  <div class="brand brand--dark" style="left:492px;top:10px;font-size:8.5px">Outpost Lattice Advisors</div>
  <div class="compare-box paper" style="left:14px;top:82px;width:316px;height:268px"></div>
  <div class="abs" style="left:94px;top:82px;width:1px;height:268px;background:#cfcbc5"></div>
  <div class="side-label side-label--up" style="left:30px;top:88px;height:256px">Internal Franchise<br>Development Director</div>
  <ul class="compare-list compare-list--light" style="left:120px;top:112px">
    <li>Recruiting costs</li><li>Salary</li><li>Benefits</li><li>Payroll taxes</li><li>Training</li><li>Ramp-up period</li><li>Unknown performance</li>
  </ul>
  <div class="compare-box navy" style="left:337px;top:82px;width:317px;height:268px"></div>
  <div class="abs" style="left:573px;top:82px;width:1px;height:268px;background:#4a5870"></div>
  <div class="side-label side-label--down" style="left:590px;top:88px;height:256px">Outpost Lattice<br>Advisors</div>
  <ul class="compare-list compare-list--dark" style="left:365px;top:112px">
    <li>Fractional investment</li><li>Entire team of experts</li><li>Immediate launch</li><li>Proven processes</li><li>Existing relationships</li><li>Scalable growth</li>
  </ul>
  <div class="pageno" style="left:640px;top:358px">04</div>
</section>

<!-- 05 day one wheel -->
<section class="slide" style="left:800.5px;top:270px">
  <h2 class="title title--dark" style="left:12px;top:10px;font-size:23px;line-height:1.17">What takes years<br>to build, <span class="hl-in">you get</span><span class="hl">on day one</span></h2>
  <div class="brand brand--dark" style="left:492px;top:10px;font-size:8.5px">Outpost Lattice Advisors</div>
  <div class="bar" style="left:40px;top:108px;width:18px;height:122px"></div>
  <div class="bar" style="left:0;top:210px;width:58px;height:20px"></div>
  <div class="bar" style="left:610px;top:244px;width:18px;height:106px"></div>
  <div class="bar" style="left:610px;top:244px;width:56px;height:18px"></div>
  <svg class="abs" style="left:0;top:0" width="666" height="375" viewBox="0 0 666 375">
    <defs><path id="seg" d="M -41.96 -103.85 A 112 112 0 0 1 41.96 -103.85 L 23.23 -57.48 A 62 62 0 0 0 -23.23 -57.48 Z"/></defs>
    <g transform="translate(334 228)">
      <use href="#seg" fill="#15243d"/>
      <use href="#seg" fill="#f5821f" transform="rotate(51.43)"/>
      <use href="#seg" fill="#15243d" transform="rotate(102.86)"/>
      <use href="#seg" fill="#f5821f" transform="rotate(154.29)"/>
      <use href="#seg" fill="#f5821f" transform="rotate(205.71)"/>
      <use href="#seg" fill="#15243d" transform="rotate(257.14)"/>
      <use href="#seg" fill="#f5821f" transform="rotate(308.57)"/>
      <g fill="none" stroke="#fff" stroke-width="2.2">
        <circle cx="0" cy="-87" r="8"/><circle cx="68" cy="-54" r="8"/><circle cx="85" cy="19" r="8"/><circle cx="38" cy="78" r="8"/><circle cx="-38" cy="78" r="8"/><circle cx="-85" cy="19" r="8"/><circle cx="-68" cy="-54" r="8"/>
      </g>
      <g fill="#fff" stroke="#15243d" stroke-width="1"><circle cx="0" cy="-112" r="7"/><circle cx="87.6" cy="-69.8" r="7"/><circle cx="109.2" cy="24.9" r="7"/><circle cx="48.6" cy="100.9" r="7"/><circle cx="-48.6" cy="100.9" r="7"/><circle cx="-109.2" cy="24.9" r="7"/><circle cx="-87.6" cy="-69.8" r="7"/></g>
      <g font-family="Open Sans" font-size="7" font-weight="700" fill="#15243d" text-anchor="middle">
        <text x="0" y="-109.5">01</text><text x="87.6" y="-67.3">02</text><text x="109.2" y="27.4">03</text><text x="48.6" y="103.4">04</text><text x="-48.6" y="103.4">05</text><text x="-109.2" y="27.4">06</text><text x="-87.6" y="-67.3">07</text>
      </g>
      <text x="0" y="3" font-family="Montserrat" font-size="7" font-weight="700" fill="#15243d" text-anchor="middle">OUTPOST LATTICE ADVISORS</text>
    </g>
  </svg>
  <div class="wheel-label" style="left:274px;top:78px">Franchise broker<br>relationships</div>
  <div class="wheel-label" style="left:435px;top:148px">Franchise sales<br>expertise</div>
  <div class="wheel-label" style="left:448px;top:236px">Lead qualification<br>systems</div>
  <div class="wheel-label" style="left:430px;top:306px">Franchise development<br>processes</div>
  <div class="wheel-label" style="left:122px;top:306px">Industry<br>connections</div>
  <div class="wheel-label" style="left:92px;top:236px">Candidate nurturing<br>systems</div>
  <div class="wheel-label" style="left:120px;top:148px">CRM and reporting<br>infrastructure</div>
  <div class="pageno" style="left:640px;top:358px">05</div>
</section>

<!-- 06 broker community -->
<section class="slide" style="left:21.5px;top:501.5px">
  <h2 class="title title--dark" style="left:12px;top:10px;font-size:21px;line-height:1.2">Instant access to <span class="hl-in">the franchise</span><span class="hl">broker community</span></h2>
  <div class="brand brand--dark" style="left:492px;top:10px;font-size:8.5px">Outpost Lattice Advisors</div>
  <p class="abs" style="left:12px;top:68px;font-size:8.5px;color:var(--ink)">We spent over 20 years building these relationships so your brand doesn't have to.</p>
  <svg class="abs" style="left:0;top:0" width="666" height="375" viewBox="0 0 666 375">
    <g stroke="#15243d" stroke-width="1.2" fill="#15243d">
      <line x1="162" y1="150" x2="180" y2="185"/><circle cx="162" cy="150" r="2.5"/>
      <line x1="280" y1="150" x2="266" y2="172"/><circle cx="280" cy="150" r="2.5"/>
      <line x1="140" y1="240" x2="164" y2="240"/><circle cx="140" cy="240" r="2.5"/>
      <line x1="302" y1="240" x2="288" y2="240"/><circle cx="302" cy="240" r="2.5"/>
      <line x1="232" y1="300" x2="232" y2="284"/><circle cx="232" cy="300" r="2.5"/>
    </g>
    <line x1="432" y1="237" x2="452" y2="237" stroke="#f5821f" stroke-width="1.5"/>
    <circle cx="452" cy="237" r="4" fill="#f5821f"/>
    <circle cx="226" cy="222" r="62" fill="#fff" stroke="#15243d" stroke-width="1.5"/>
    <circle cx="226" cy="222" r="53" fill="#cfcac3"/>
    <text x="226" y="225" font-family="Montserrat" font-size="7" font-weight="700" fill="#15243d" text-anchor="middle">OUTPOST LATTICE ADVISORS</text>
  </svg>
  <div class="node" style="left:32px;top:118px;width:130px;padding-left:58px">Franchise<br>consultants</div>
  <div class="node-icon" style="left:34px;top:117px"><svg width="24" height="24" viewBox="0 0 24 24" fill="#fff"><rect x="6" y="2" width="12" height="8" rx="1"/><circle cx="6" cy="15" r="3"/><circle cx="18" cy="15" r="3"/><path d="M1 24c0-5 10-5 10 0zM13 24c0-5 10-5 10 0z"/></svg></div>
  <div class="node" style="left:280px;top:118px;width:130px;padding-left:20px">Referral<br>sources</div>
  <div class="node-icon" style="left:354px;top:117px"><svg width="24" height="24" viewBox="0 0 24 24" fill="#fff"><circle cx="12" cy="5" r="4"/><circle cx="4" cy="18" r="4"/><circle cx="20" cy="18" r="4"/><path d="M12 5L4 18H20Z" fill="none" stroke="#fff" stroke-width="2"/></svg></div>
  <div class="node" style="left:12px;top:212px;width:128px;padding-left:62px">Franchise<br>influencers</div>
  <div class="node-icon" style="left:12px;top:211px"><svg width="24" height="24" viewBox="0 0 24 24" fill="#fff"><circle cx="12" cy="12" r="11" fill="none" stroke="#fff" stroke-width="2"/><circle cx="12" cy="9" r="4"/><path d="M5 19c2-5 12-5 14 0z"/></svg></div>
  <div class="node" style="left:302px;top:212px;width:130px;padding-left:20px">Broker<br>networks</div>
  <div class="node-icon" style="left:376px;top:211px"><svg width="24" height="24" viewBox="0 0 24 24" fill="#fff"><circle cx="12" cy="4" r="3.5"/><circle cx="4" cy="19" r="3.5"/><circle cx="12" cy="19" r="3.5"/><circle cx="20" cy="19" r="3.5"/><path d="M12 8v4M4 12h16M4 12v4M20 12v4M12 12v4" stroke="#fff" stroke-width="2"/></svg></div>
  <div class="node" style="left:154px;top:300px;width:130px;padding-left:60px">Industry<br>partners</div>
  <div class="node-icon" style="left:154px;top:299px"><svg width="24" height="24" viewBox="0 0 24 24" fill="#fff"><path d="M1 10l6-4 5 3 5-3 6 4-6 7-5-3-5 3z"/></svg></div>
  <div class="eco-table" style="left:452px;top:60px;width:156px;height:292px">
    <div class="eco-head">Broker Network<br>Ecosystem</div>
    <div class="eco-row">KESTRELNET</div><div class="eco-row">ALDERWAY</div><div class="eco-row">BRIGHTLINE</div><div class="eco-row">MERIDIAN</div><div class="eco-row">CORALPATH</div><div class="eco-row">NORTHGATE</div>
  </div>
  <div class="bar" style="left:640px;top:162px;width:16px;height:213px"></div>
  <div class="bar" style="left:610px;top:162px;width:46px;height:16px"></div>
  <div class="pageno" style="left:640px;top:358px">06</div>
</section>

<!-- 07 process -->
<section class="slide" style="left:411px;top:501.5px">
  <div class="photo" role="img" aria-label="Navy-tinted photo of business people talking in a modern lobby" style="left:0;top:0;width:276px;height:375px;background:linear-gradient(160deg,#2a3953 0%,#1b2a43 55%,#15243d 100%)"></div>
  <div class="bar" style="left:0;top:10px;width:56px;height:20px"></div>
  <div class="bar" style="left:36px;top:10px;width:20px;height:92px"></div>
  <h2 class="title" style="left:10px;top:150px;font-size:22px;line-height:1.17">Our<br>franchise<span class="hl">development</span><span class="hl">process</span></h2>
  <div class="brand brand--dark" style="left:492px;top:10px;font-size:8.5px">Outpost Lattice Advisors</div>
  <div class="rule" style="left:314px;top:296px;width:170px;height:1px"></div>
  <div class="rule" style="left:483px;top:127px;width:1px;height:170px"></div>
  <div class="step" style="left:305px;top:25px;width:160px;height:80px"><h4>1. Lead</h4><p>Short summary of this step and what it covers for the brand.</p></div>
  <div class="step" style="left:305px;top:110px;width:160px;height:80px"><h4>2. Qualification</h4><p>Short summary of this step and what it covers for the brand.</p></div>
  <div class="step" style="left:305px;top:195px;width:160px;height:80px"><h4>3. Education</h4><p>Short summary of this step and what it covers for the brand.</p></div>
  <div class="step" style="left:305px;top:280px;width:160px;height:78px"><h4>4. FDD Review</h4><p>Short summary of this step and what it covers for the brand.</p></div>
  <div class="step" style="left:472px;top:110px;width:160px;height:80px"><h4>7. Franchise Award</h4><p>Short summary of this step and what it covers for the brand.</p></div>
  <div class="step" style="left:472px;top:195px;width:160px;height:80px"><h4>6. Discovery Day</h4><p>Short summary of this step and what it covers for the brand.</p></div>
  <div class="step" style="left:472px;top:280px;width:160px;height:78px"><h4>5. Validation</h4><p>Short summary of this step and what it covers for the brand.</p></div>
  <div class="rule" style="left:314px;top:42px;width:1px;height:254px"></div>
  <div class="dot" style="left:312px;top:41px"></div><div class="dot" style="left:312px;top:126px"></div><div class="dot" style="left:312px;top:211px"></div><div class="dot" style="left:312px;top:294px"></div>
  <div class="dot" style="left:481px;top:126px"></div><div class="dot" style="left:481px;top:211px"></div><div class="dot" style="left:481px;top:294px"></div>
  <div class="pageno" style="left:640px;top:358px">07</div>
</section>

<!-- 08 services -->
<section class="slide navy" style="left:800.5px;top:501.5px">
  <div class="bar" style="left:22px;top:0;width:18px;height:56px"></div>
  <div class="bar" style="left:22px;top:38px;width:86px;height:18px"></div>
  <div class="bar" style="left:520px;top:38px;width:122px;height:18px"></div>
  <div class="bar" style="left:624px;top:38px;width:18px;height:90px"></div>
  <div class="bar" style="left:622px;top:335px;width:20px;height:40px"></div>
  <div class="brand" style="left:492px;top:10px;font-size:8.5px">Outpost Lattice Advisors</div>
  <h2 class="title" style="left:0;top:32px;width:666px;text-align:center;font-size:23px">Services we <span class="hl-in">provide</span></h2>
  <div class="card" style="left:10px;top:96px;width:155px;height:118px"><svg class="ico" width="20" height="18" viewBox="0 0 20 18" fill="#15243d"><path d="M0 0h14v10H5l-5 4z"/><circle cx="16" cy="4" r="4"/></svg><h4>Broker/Consultant education</h4><p>Short summary of this step and what it covers for the brand.</p></div>
  <div class="card" style="left:174px;top:96px;width:155px;height:118px"><svg class="ico" width="22" height="18" viewBox="0 0 22 18" fill="#15243d"><circle cx="6" cy="5" r="4"/><circle cx="16" cy="5" r="4"/><path d="M0 18c0-7 12-7 12 0zM10 18c0-7 12-7 12 0z"/></svg><h4>Franchise sales outsourcing</h4><p>Short summary of this step and what it covers for the brand.</p></div>
  <div class="card" style="left:337px;top:96px;width:155px;height:118px"><svg class="ico" width="20" height="18" viewBox="0 0 20 18" fill="#15243d"><circle cx="6" cy="4" r="3.5"/><circle cx="14" cy="4" r="3.5"/><rect x="1" y="8" width="18" height="4"/><rect x="8.5" y="12" width="3" height="6"/></svg><h4>Lead qualification</h4><p>Short summary of this step and what it covers for the brand.</p></div>
  <div class="card" style="left:500px;top:96px;width:155px;height:118px"><svg class="ico" width="20" height="18" viewBox="0 0 20 18" fill="#15243d"><circle cx="10" cy="4" r="3.5"/><path d="M0 10l5-2 5 4 5-4 5 2-10 8z"/></svg><h4>Candidate nurturing</h4><p>Short summary of this step and what it covers for the brand.</p></div>
  <div class="card" style="left:10px;top:224px;width:155px;height:118px"><svg class="ico" width="20" height="18" viewBox="0 0 20 18" fill="#15243d"><circle cx="10" cy="4" r="3.5"/><circle cx="3.5" cy="14" r="3.5"/><circle cx="16.5" cy="14" r="3.5"/><path d="M10 4L3.5 14h13z" fill="none" stroke="#15243d" stroke-width="1.6"/></svg><h4>Discovery day coordination</h4><p>Short summary of this step and what it covers for the brand.</p></div>
  <div class="card" style="left:174px;top:224px;width:155px;height:118px"><svg class="ico" width="20" height="18" viewBox="0 0 20 18"><circle cx="8" cy="7" r="6" fill="none" stroke="#15243d" stroke-width="2"/><path d="M12.5 11.5L19 17.5" stroke="#15243d" stroke-width="2.6"/></svg><h4>Broker recruitment / engagement</h4><p>Short summary of this step and what it covers for the brand.</p></div>
  <div class="card" style="left:337px;top:224px;width:155px;height:118px"><svg class="ico" width="20" height="18" viewBox="0 0 20 18" fill="#15243d"><rect x="2" y="0" width="13" height="17" rx="1"/><rect x="5" y="4" width="7" height="1.5" fill="#efedea"/><rect x="5" y="8" width="7" height="1.5" fill="#efedea"/><rect x="5" y="12" width="5" height="1.5" fill="#efedea"/></svg><h4>CRM management</h4><p>Short summary of this step and what it covers for the brand.</p></div>
  <div class="card" style="left:500px;top:224px;width:155px;height:118px"><svg class="ico" width="20" height="18" viewBox="0 0 20 18" fill="#15243d"><rect x="0" y="2" width="14" height="14" rx="1"/><rect x="3" y="9" width="2" height="5" fill="#efedea"/><rect x="6.5" y="6" width="2" height="8" fill="#efedea"/><rect x="10" y="4" width="2" height="10" fill="#efedea"/><circle cx="16" cy="14" r="4"/></svg><h4>Reporting and forecasting</h4><p>Short summary of this step and what it covers for the brand.</p></div>
  <div class="pageno" style="left:627px;top:358px;color:var(--white)">08</div>
</section>

<!-- 09 referral engine -->
<section class="slide navy" style="left:21.5px;top:730.9px">
  <div class="bar" style="left:24px;top:0;width:20px;height:44px"></div>
  <div class="bar" style="left:24px;top:24px;width:96px;height:20px"></div>
  <div class="bar" style="left:622px;top:0;width:20px;height:108px"></div>
  <div class="bar" style="left:622px;top:345px;width:20px;height:30px"></div>
  <div class="brand" style="left:492px;top:10px;font-size:8.5px">Outpost Lattice Advisors</div>
  <h2 class="title" style="left:0;top:32px;width:666px;text-align:center;font-size:22px;line-height:1.2">Building a <span class="hl-in">referral</span><span class="hl">engine for your brand</span></h2>
  <div class="card" style="left:10px;top:108px;width:155px;height:238px"><svg class="ico" width="26" height="20" viewBox="0 0 26 20" fill="#15243d"><path d="M13 0L26 6 13 12 0 6z"/><path d="M5 9v6c4 4 12 4 16 0V9l-8 4z"/></svg><h4>Broker/Consultant education</h4><p>Short summary of this step and what it covers for the brand.</p><p>Longer note on how this part of the program works, who takes part, what the franchisor receives and how results are tracked over time as new owners join the system and refer others.</p></div>
  <div class="card" style="left:174px;top:108px;width:155px;height:238px"><svg class="ico" width="26" height="20" viewBox="0 0 26 20"><rect x="2" y="1" width="22" height="14" fill="none" stroke="#15243d" stroke-width="2"/><rect x="7" y="8" width="2" height="5" fill="#15243d"/><rect x="12" y="5" width="2" height="8" fill="#15243d"/><rect x="17" y="7" width="2" height="6" fill="#15243d"/><path d="M9 15l-3 5M17 15l3 5" stroke="#15243d" stroke-width="2"/></svg><h4>Brand presentations</h4><p>Short summary of this step and what it covers for the brand.</p><p>Longer note on how this part of the program works, who takes part, what the franchisor receives and how results are tracked over time as new owners join the system and refer others.</p></div>
  <div class="card" style="left:337px;top:108px;width:155px;height:238px"><svg class="ico" width="26" height="22" viewBox="0 0 26 22" fill="#15243d"><rect x="8" y="0" width="10" height="7" rx="1"/><circle cx="6" cy="12" r="3"/><circle cx="20" cy="12" r="3"/><path d="M0 22c0-6 12-6 12 0zM14 22c0-6 12-6 12 0z"/></svg><h4>Ongoing communication</h4><p>Short summary of this step and what it covers for the brand.</p><p>Longer note on how this part of the program works, who takes part, what the franchisor receives and how results are tracked over time as new owners join the system and refer others.</p></div>
  <div class="card" style="left:500px;top:108px;width:155px;height:238px"><svg class="ico" width="24" height="22" viewBox="0 0 24 22" fill="none" stroke="#15243d" stroke-width="2.6"><path d="M10 14l-3 3a4 4 0 0 1-6-6l3-3M14 8l3-3a4 4 0 0 1 6 6l-3 3M8 14l8-8"/></svg><h4>Referral generation</h4><p>Short summary of this step and what it covers for the brand.</p><p>Longer note on how this part of the program works, who takes part, what the franchisor receives and how results are tracked over time as new owners join the system and refer others.</p></div>
  <div class="pageno" style="left:626px;top:358px">09</div>
</section>

<!-- 10 case study -->
<section class="slide" style="left:411px;top:730.9px">
  <div class="abs navy" style="left:0;top:0;width:371px;height:375px"></div>
  <h2 class="title" style="left:12px;top:20px;font-size:23px;line-height:1.17">Success stories<span class="hl">Case study #1</span></h2>
  <div class="bar" style="left:57px;top:87px;width:20px;height:288px"></div>
  <div class="story" style="left:102px;top:112px;width:232px">
    <h3>A regional brand doubled its signed units in eighteen months.</h3>
    <p>The client came to us with a proven concept, a small corporate team and no dedicated sales staff. We took over lead handling, rebuilt the qualification steps, opened doors with our broker partners and ran every discovery day. Within the first year the pipeline grew steadily and the founder could focus on operations again.</p>
    <p>Lead response times dropped to under a day, validation calls were scheduled for every candidate and the award rate rose month over month across all target regions.</p>
    <p>Today the brand has a steady flow of qualified buyers, a clear reporting rhythm and a growth story that investors can follow with confidence.</p>
  </div>
  <div class="brand brand--dark" style="left:492px;top:10px;font-size:8.5px">Outpost Lattice Advisors</div>
  <div class="photo" role="img" aria-label="Photo of two colleagues reviewing results on a laptop in an office" style="left:389px;top:55px;width:231px;height:283px;background:linear-gradient(160deg,#dfe3e6 0%,#b9c1c8 45%,#6e7a86 100%)"></div>
  <div class="bar" style="left:620px;top:285px;width:20px;height:90px"></div>
  <div class="pageno" style="left:624px;top:358px">02</div>
</section>

<!-- 11 closing -->
<section class="slide navy" style="left:800.5px;top:730.9px">
  <div class="photo" role="img" aria-label="Photo of a smiling businessman reviewing papers at a desk" style="left:300px;top:0;width:366px;height:375px;background:linear-gradient(90deg,#15243d 0%,#2e3a4d 40%,#5b5a56 75%,#8a7f72 100%)"></div>
  <div class="brand" style="left:40px;top:30px">Outpost Lattice Advisors</div>
  <div class="bar" style="left:24px;top:90px;width:20px;height:65px"></div>
  <div class="bar" style="left:24px;top:135px;width:56px;height:20px"></div>
  <div class="bar" style="left:425px;top:0;width:20px;height:160px"></div>
  <div class="bar" style="left:305px;top:140px;width:140px;height:20px"></div>
  <h2 class="title" style="left:88px;top:102px;font-size:25px;line-height:1.05">Let's build <span class="hl-in">your</span><span class="hl">growth plan</span></h2>
  <p class="meta" style="left:88px;top:172px;font-size:10.5px">Schedule a Franchise Growth Strategy Consultation</p>
  <p class="meta" style="left:88px;top:214px;font-size:10.5px">Call Us:<br>+1 555-010-0199</p>
  <p class="meta" style="left:88px;top:257px;font-size:10.5px">Visit Us:<br>www.outpostlatticeadvisors.example</p>
</section>

</body>
</html>
```